Poster Design

Hello,

My name is Rowan Pickett and I run a vidora channel called 'CrumbleDiary'. I want a poster made for those who watch my video to purchase and put on their wall at home. The poster will be all text and as you can see, I've attached a few examples of posters which I would like it to be similar to. I use a lot of the colour #ab6f7f so it would be good to incorporate this in somewhere (maybe the background colour).
I would like the poster to say:
"Do More Of What Makes YOU Happy"
I need this poster to be for sale ready for christmas, so Im going to need the designs created as soon as possible. Im sorry for the rush.
Have fun with it and feel free to upload multiple versions of a design as well as a few designs if you like.
I look forward to seeing what you come up with.
Rowan
(Of course I will need to own all rights once the payment has been made)

```html
<!DOCTYPE html>
<html lang="en">
<head>
<meta charset="utf-8">
<title>Do More Of What Makes You Happy – Poster</title>
<link rel="stylesheet" href="https://fonts.googleapis.com/css2?family=Alfa+Slab+One&family=Anton&family=Oswald:wght@600&display=swap">
<style>
  :root {
    --paper: #f1d6de;
    --mauve: #8d4862;
    --mauve-band: #a5637b;
    --rule: #b7778d;
    --ink-light: #ebc7d3;
    --ink-shade: #c996a8;
    --ink-dark: #4b2334;
  }
  * { margin: 0; padding: 0; box-sizing: border-box; }
  html, body {
    width: 854px; height: 1200px; overflow: hidden;
    background: var(--paper);
  }
  .poster {
    position: relative;
    width: 854px; height: 1200px;
    background: var(--paper);
  }
  .poster__panel {
    position: absolute;
    left: 14px; top: 14px; width: 826px; height: 1167px;
    background: var(--mauve);
  }
  .poster__footer-band {
    position: absolute;
    left: 14px; top: 1110px; width: 826px; height: 71px;
    background: var(--mauve-band);
  }
  .poster__tab {
    position: absolute;
    left: 826px; top: 887px; width: 28px; height: 162px;
    background: var(--mauve);
    border-radius: 0 12px 12px 0;
  }
  .rule {
    position: absolute; height: 6px; background: var(--rule);
  }
  .rule--top-a { left: 157px; top: 57px; width: 623px; }
  .rule--top-b { left: 71px;  top: 72px; width: 627px; }
  .rule--bottom-a { left: 171px; top: 1053px; width: 626px; }
  .rule--bottom-b { left: 90px;  top: 1070px; width: 626px; }
  .dash {
    position: absolute; width: 92px; height: 5px; background: var(--ink-dark);
  }
  .dash--left-a  { left: 28px;  top: 402px; }
  .dash--left-b  { left: 28px;  top: 416px; }
  .dash--right-a { left: 731px; top: 402px; }
  .dash--right-b { left: 731px; top: 416px; }

  .line {
    position: absolute; left: 0; width: 854px;
    text-align: center; line-height: 1; white-space: nowrap;
    text-transform: uppercase;
  }
  .line--engraved {
    font-family: "Alfa Slab One", serif;
    color: var(--ink-light);
    text-shadow:
      2px 2px 0 var(--mauve), 3px 3px 0 var(--ink-shade),
      5px 5px 0 var(--mauve), 6px 6px 0 var(--ink-shade),
      8px 8px 0 var(--mauve), 9px 9px 0 var(--ink-shade);
  }
  .line--do-more { top: 178px; font-size: 124px; letter-spacing: 2px; padding-left: 20px; }
  .line--of-what {
    top: 326px; font-family: "Anton", sans-serif; font-size: 188px;
    color: var(--ink-dark); letter-spacing: -4px; transform: scaleY(0.88);
    padding-right: 24px;
  }
  .line--makes {
    top: 540px; font-family: "Oswald", sans-serif; font-weight: 600;
    font-size: 80px; color: var(--ink-light); letter-spacing: 3px; padding-left: 76px;
  }
  .line--you { top: 645px; font-size: 226px; letter-spacing: 4px; padding-right: 10px; }
  .line--happy { top: 886px; font-size: 150px; letter-spacing: 6px; padding-left: 44px; }
</style>
</head>
<body>
  <main class="poster">
    <div class="poster__panel"></div>
    <div class="poster__footer-band"></div>
    <div class="poster__tab"></div>

    <div class="rule rule--top-a"></div>
    <div class="rule rule--top-b"></div>

    <div class="dash dash--left-a"></div>
    <div class="dash dash--left-b"></div>
    <div class="dash dash--right-a"></div>
    <div class="dash dash--right-b"></div>

    <h1 class="headline">
      <span class="line line--engraved line--do-more">Do More</span>
      <span class="line line--of-what">Of What</span>
      <span class="line line--makes">Makes</span>
      <span class="line line--engraved line--you">You</span>
      <span class="line line--engraved line--happy">Happy</span>
    </h1>

    <div class="rule rule--bottom-a"></div>
    <div class="rule rule--bottom-b"></div>
  </main>
</body>
</html>
```